The Brambury Firm

We need a new design for our letterhead and envelopes. We are a personal injury and criminal defense firm so we need something modern and clean, but more on the professional/traditional side. Our new logo has two colors and is attached to the file so we need something that works well with those colors/matches the design. The following information needs to be on the letterhead:
Phone: (555) 314-7265
Fax: (555) 419-6032
Toll-Free: (555) 736-1149
Post Office Box 4273
Harlow Bend, TQ 29458-4273
TQHarmClaimsDesk.example
PalmettoShieldCounsel.example

Target Market(s)

Clients, government agencies, other law firms

Industry/Entity Type

Legal

Font styles to use
Sans Serif
Other font styles liked:
• Arial

Colors

Designer to choose colors to be used in the design.

Requirements
Must have
• Must look professional and clean, modern
Nice to have
• I would like to see a design that works with the logo but does not distract from the content that will be printed on it
Should not have
• Too many colors or crazy designs.

```html
<!DOCTYPE html>
<html lang="en">
<head>
<meta charset="utf-8">
<title>The Brambury Firm — Letterhead</title>
<link rel="stylesheet" href="https://fonts.googleapis.com/css2?family=Jost:wght@400;500;600&family=Lexend:wght@500;600&display=swap">
<style>
  :root {
    --brand-red: #d71f26;
    --brand-navy: #2b3190;
    --ink: #2a2a2a;
    --page: #ffffff;
    --backdrop: #f6f6f6;
    --edge: #e2e2e2;
  }
  * { box-sizing: border-box; margin: 0; padding: 0; }
  html, body { width: 1200px; height: 1200px; overflow: hidden; }
  body { background: var(--backdrop); font-family: "Jost", Arial, sans-serif; color: var(--ink); position: relative; }

  .brand-mark {
    position: absolute; top: 160px; left: 0; width: 1200px; text-align: center;
    font-family: "Lexend", Arial, sans-serif; font-weight: 600; font-size: 46px;
    color: var(--brand-navy); letter-spacing: 1px;
  }
  .brand-mark .dot {
    display: inline-block; width: 22px; height: 22px; border-radius: 50%;
    background: var(--brand-navy); margin-right: 14px; vertical-align: 4px;
  }

  .sheet {
    position: absolute; top: 454px; width: 510px; height: 659px;
    background: var(--page); border: 1px solid var(--edge);
  }
  .sheet--letter { left: 68px; }
  .sheet--blank { left: 625px; }

  .sheet-logo {
    position: absolute; left: 50px; top: 58px;
    font-family: "Lexend", Arial, sans-serif; font-weight: 600; font-size: 14px;
    color: var(--brand-navy); white-space: nowrap;
  }
  .sheet-logo .dot {
    display: inline-block; width: 9px; height: 9px; border-radius: 50%;
    background: var(--brand-navy); margin-right: 6px; vertical-align: 1px;
  }

  .contact {
    position: absolute; left: 312px; top: 31px;
    font-size: 8.8px; font-weight: 600; line-height: 10.5px; color: #1e1e1e;
  }
  .contact p + p { margin-top: 6px; }

  .headline {
    position: absolute; left: 74px; top: 216px;
    font-family: "Lexend", Arial, sans-serif; font-weight: 600; font-size: 24px;
    color: var(--brand-red);
  }
  .body-copy {
    position: absolute; left: 74px; top: 263px; width: 398px;
    font-size: 10.5px; line-height: 13.8px; color: #333;
  }
  .body-copy p + p { margin-top: 13.8px; }

  .signoff { position: absolute; left: 325px; top: 496px; font-family: "Lexend", Arial, sans-serif; }
  .sheet--blank .signoff { top: 498px; }
  .signoff .role { font-size: 14px; font-weight: 500; color: #2e2e2e; }
  .signoff .name { font-size: 11.5px; font-weight: 600; color: var(--brand-red); margin-top: 3px; }
</style>
</head>
<body>

  <div class="brand-mark"><span class="dot"></span>The Brambury Firm</div>

  <section class="sheet sheet--letter">
    <div class="sheet-logo"><span class="dot"></span>The Brambury Firm</div>
    <div class="contact">
      <p>Post Office Box 4273<br>Harlow Bend, TQ 29458-4273</p>
      <p>Phone: (555) 314-7265<br>Fax: (555) 419-6032<br>Toll-Free: (555) 736-1149</p>
      <p>TQHarmClaimsDesk.example<br>PalmettoShieldCounsel.example</p>
    </div>
    <h1 class="headline">Headline</h1>
    <div class="body-copy">
      <p>Lorem ipsum dolor sit amet, consectetur adipiscing elit. Fusce dignissim pretium consectetur. Curabitur tempor posuere massa in varius. Pellentesque viverra nibh eu vehicula mattis. Nullam porta facilisis justo, a feugiat dolor sodales sed. Vestibulum neque nisi, elementum tincidunt metus sit amet, egestas bibendum enim. Aenean a blandit elit, vel rutrum mi. Nunc dapibus turpis sed massa aliquet tincidunt.</p>
      <p>Pellentesque id neque ligula. Nullam posuere, ligula a mattis posuere, lacus nisl adipiscing nunc, eu congue justo est ut diam. Nam quam nibh, dignissim non consequat in, semper eget purus. Nulla arcu sapien, viverra vitae metus tempor, congue ornare diam.</p>
      <p>Pellentesque vel nibh tempus, ullamcorper tortor sed, bibendum augue. Phasellus sollicitudin justo et quam aliquam sollicitudin. Sed eget nibh mollis, mattis sem et, viverra nulla.</p>
    </div>
    <div class="signoff">
      <div class="role">Managing Director</div>
      <div class="name">Name or signature</div>
    </div>
  </section>

  <section class="sheet sheet--blank">
    <div class="sheet-logo"><span class="dot"></span>The Brambury Firm</div>
    <div class="contact">
      <p>Post Office Box 4273<br>Harlow Bend, TQ 29458-4273</p>
      <p>Phone: (555) 314-7265<br>Fax: (555) 419-6032<br>Toll-Free: (555) 736-1149</p>
      <p>TQHarmClaimsDesk.example<br>PalmettoShieldCounsel.example</p>
    </div>
    <div class="signoff">
      <div class="role">Managing Director</div>
      <div class="name">Name or signature</div>
    </div>
  </section>

</body>
</html>
```